QORLIN Business card. A.I. company developing trading strategies.

My name is marcello bianchi and I'm CEO and co-founder of QORLIN Research, an AI company focusing on generating Ai-driven trading strategies.
This is our website: https://qorlin-analytics.example/
Values of our company: tech & R&D driven (we're all very mathy/stats/data driven), sophisticated (we only look for sophisticated, high knowledge investors), reserved (we don't go around telling anyone what we do).
Our main product: PivotFund. A trading strategy that delivered 70% in 2022 and 20% in 2023 so far.
Our main potential clients: HNW individuals, hedge funds, asset managers, tech entrepreneur.
Target Market(s)
Hedge funds, asset managers, High Net Worth individuals, Pension funds
Contact Information for Business Card
The basic: name, job title, company name, address, mail, phone number

```html
<!DOCTYPE html>
<html lang="en">
<head>
<meta charset="UTF-8">
<title>QORLIN Research — Business Card</title>
<link rel="stylesheet" href="https://fonts.googleapis.com/css2?family=Raleway:ital,wght@0,300;0,400;0,700;0,800;1,300;1,400&display=swap">
<style>
  :root {
    --stage: #e4e4e2;
    --card-light: #ffffff;
    --card-dark: #1c1d20;
    --card-dark-glow: #30323a;
    --ink: #231f20;
    --ink-soft: #3a3a3a;
    --accent: #b3203f;
    --pattern-light: #e6e6e8;
    --pattern-dark: #3a3c44;
    --link-light: #c9c9cc;
  }
  * { box-sizing: border-box; margin: 0; padding: 0; }
  html, body {
    width: 1200px; height: 846px; overflow: hidden;
    background: var(--stage);
    font-family: "Raleway", sans-serif;
  }
  .canvas { position: relative; width: 1200px; height: 846px; }

  .card {
    position: absolute; left: 346px; width: 508px; height: 290px; overflow: hidden;
  }
  .card--front { top: 99px; background: var(--card-light); }
  .card--back {
    top: 456px;
    background: radial-gradient(ellipse at 95% 10%, var(--card-dark-glow) 0%, var(--card-dark) 60%, #121315 100%);
  }

  .pattern { position: absolute; }
  .card--front .pattern {
    top: 0; right: 0; width: 330px; height: 290px;
    background: linear-gradient(90deg, rgba(230,230,232,0) 0%, var(--pattern-light) 70%, #dcdcdf 100%);
  }
  .card--back .pattern {
    top: 0; right: 0; width: 470px; height: 290px;
    background: linear-gradient(100deg, rgba(58,60,68,0) 0%, rgba(58,60,68,.55) 45%, rgba(70,72,80,.65) 100%);
  }

  .wordmark {
    position: absolute; display: flex; align-items: flex-start; gap: 5px;
    font-weight: 300; letter-spacing: 4px; line-height: 1;
  }
  .wordmark__dot { width: 5px; height: 5px; border-radius: 50%; background: var(--accent); margin-top: 2px; }
  .card--front .wordmark { left: 36px; top: 40px; font-size: 48px; color: var(--ink); }
  .card--back .wordmark { left: 31px; top: 205px; font-size: 40px; color: #ffffff; }

  .contact { position: absolute; left: 35px; top: 136px; color: var(--ink-soft); }
  .contact__name { font-size: 16px; font-weight: 800; color: var(--accent); }
  .contact__role { font-size: 13.5px; font-style: italic; font-weight: 400; margin-top: 3px; color: var(--ink); }
  .contact__details { list-style: none; margin-top: 12px; font-size: 13.5px; font-weight: 300; line-height: 18.3px; color: var(--ink); }
  .contact__web { font-weight: 800; color: var(--accent); }

  .back__web {
    position: absolute; right: 28px; top: 248px;
    font-size: 13px; font-weight: 700; color: var(--link-light); letter-spacing: .2px;
  }
</style>
</head>
<body>
<main class="canvas">
  <section class="card card--front" aria-label="Business card front">
    <div class="pattern" role="img" aria-label="Light grey circuit-board traces blending into fine wave lines"></div>
    <div class="wordmark">QORLIN<span class="wordmark__dot"></span></div>
    <div class="contact">
      <p class="contact__name">Marcello Bianchi</p>
      <p class="contact__role">Co-Founder &amp; CEO</p>
      <ul class="contact__details">
        <li>SIREN Number: 512604388</li>
        <li>info@qorlin-analytics.example</li>
        <li class="contact__web">www.qorlin-analytics.example</li>
        <li>48 rue des Lilas 75011 Paris</li>
      </ul>
    </div>
  </section>

  <section class="card card--back" aria-label="Business card back">
    <div class="pattern" role="img" aria-label="Grey circuit-board traces and fine wave mesh on dark background"></div>
    <div class="wordmark">QORLIN<span class="wordmark__dot"></span></div>
    <p class="back__web">www.qorlin-analytics.example</p>
  </section>
</main>
</body>
</html>
```